Fresh & clean business card for yacht detailing company
Gullrock detailing
Professional
Captain Morgan tellaver
President
PO box 827 Speonk, ny 11846
Morgan@Gullrockdetailing.com
Gullrockdetailing.com
mtellaver mtellaver
pixelharborworks: #271 - i really like this design, can you add a touch of silver/gray to it?
quillmotionlab: #140 - i really like the back with the logo splitting the blue on bottom & black on top. #142 - i really like the front with the logo in the color at the bottom. can you take the back of #140, put it with the front of #142. Id like to see the color at the bottom in blue and another draft in black?
#34 - maybe a slightly larger logo on front of card?

```html
<!DOCTYPE html>
<html lang="en">
<head>
<meta charset="utf-8">
<title>Gullrock Detailing — Business Card</title>
<link rel="stylesheet" href="https://fonts.googleapis.com/css2?family=Open+Sans:ital,wght@0,400;0,600;0,700;1,600&display=swap">
<style>
  :root {
    --backdrop: #d9dadc;
    --card: #ffffff;
    --navy: #1f3f8f;
    --ink: #1c1c1c;
    --muted: #5b5f66;
    --silver: #a9adb3;
  }
  * { box-sizing: border-box; margin: 0; padding: 0; }
  html, body { width: 1200px; height: 878px; overflow: hidden; }
  body {
    background: var(--backdrop);
    font-family: "Open Sans", Arial, sans-serif;
    display: flex;
    align-items: center;
    justify-content: center;
    gap: 40px;
  }
  .card {
    position: relative;
    width: 540px;
    height: 309px;
    background: var(--card);
    box-shadow: 0 6px 18px rgba(0,0,0,.18);
    overflow: hidden;
  }
  .brand { position: absolute; }
  .brand-name {
    display: flex;
    align-items: center;
    gap: 9px;
    font-size: 24px;
    font-weight: 700;
    color: var(--navy);
    letter-spacing: .5px;
    line-height: 1;
  }
  .brand-mark {
    width: 13px; height: 13px;
    background: var(--navy);
    flex: none;
  }
  .brand-tagline {
    margin-top: 6px;
    font-size: 10px;
    font-weight: 600;
    font-style: italic;
    color: var(--ink);
    letter-spacing: .3px;
  }
  .front .brand { left: 34px; top: 34px; }
  .contacts {
    position: absolute;
    left: 38px; top: 104px;
    list-style: none;
    font-size: 11px;
    color: var(--muted);
    line-height: 16px;
  }
  .contacts li { display: flex; align-items: center; gap: 6px; }
  .contacts svg { width: 9px; height: 9px; fill: var(--navy); flex: none; }
  .person {
    position: absolute;
    left: 332px; top: 138px;
  }
  .person-name { font-size: 16px; font-weight: 600; color: var(--navy); }
  .person-role { font-size: 11px; color: var(--muted); margin-top: 1px; }
  .address {
    position: absolute;
    left: 300px; top: 226px;
    font-size: 11px;
    color: var(--muted);
    line-height: 15px;
  }
  .swoosh { position: absolute; inset: 0; width: 100%; height: 100%; }
  .back .brand {
    left: 50%; top: 50%;
    transform: translate(-50%, -50%);
    text-align: center;
  }
  .back .brand-name { font-size: 28px; }
</style>
</head>
<body>
  <section class="card front" aria-label="Card front">
    <svg class="swoosh" viewBox="0 0 540 309" aria-hidden="true">
      <path d="M0 212 C120 262 250 292 410 309 L0 309 Z" fill="var(--navy)"/>
      <path d="M0 202 C140 258 300 292 540 302" fill="none" stroke="var(--ink)" stroke-width="3"/>
      <path d="M0 193 C150 248 320 282 540 290" fill="none" stroke="var(--silver)" stroke-width="1.5"/>
    </svg>
    <div class="brand">
      <div class="brand-name"><span class="brand-mark"></span>Gullrock Detailing</div>
      <div class="brand-tagline">Professional Polishing &amp; Yacht Maintenance</div>
    </div>
    <ul class="contacts">
      <li><svg viewBox="0 0 10 10"><path d="M2 0h2l1 3-1.3 1a6 6 0 0 0 2.3 2.3L7 5l3 1v2c0 1-1 2-2 2C4 10 0 6 0 2 0 1 1 0 2 0z"/></svg>555 014 2738</li>
      <li><svg viewBox="0 0 10 10"><rect x="0" y="3" width="10" height="7"/><rect x="2" y="0" width="6" height="3"/></svg>555 014 2739</li>
      <li><svg viewBox="0 0 10 10"><path d="M0 1h10v8H0z M0 1l5 4 5-4" /></svg>hello@gullrockdetailing.com</li>
    </ul>
    <div class="person">
      <div class="person-name">Elias Brandmoor</div>
      <div class="person-role">Managing Director</div>
    </div>
    <address class="address" style="font-style:normal">
      P.O Box Harborline St<br>Bayview City Country 518
    </address>
  </section>

  <section class="card back" aria-label="Card back">
    <div class="brand">
      <div class="brand-name"><span class="brand-mark"></span>Gullrock Detailing</div>
      <div class="brand-tagline">Professional Polishing &amp; Yacht Maintenance</div>
    </div>
  </section>
</body>
</html>
```